Store Front Window Design

We have a beautiful corner store front dental practice with no window signage. Crazy I know...that's why we need your help.

The final design will be done in all vinyl unless unless you suggest a different medium (meaning we are open to some design idea like using frosted glass, etc...).

The windows provide a lot of natural light so the design needs to keep a lot of natural light coming into the office. Keep in mind vinyl is not opaque so keep the signage aesthetically pleasing and a minimalist design to allow as much natural light in as possible. The design should follow the aesthetic from our logo. or tie into at least. We want a cohesive brand aesthetic.

I submitted some general layout ideas. There is a blue banner with advertising words which we want to be used in the final version. Even though the lettering is black, in reality the letters will be a white vinyl on the outside of the window. When you submit your work, be sure to add any special instructions (aka tell me the vision for the letters is white not black, maybe gold leaf, or forested glass...stuff like that). AND YOU DO NOT HAVE TO FOLLOW MY PATTERN! YOU ARE ARTISTS AND WE ARE LOOKING FOR AN ARTISTIC EYE CATCHING PRESENTATION OF THIS INFORMATION. MAKE IT FLASHY AND ADD SOME AESTHETIC FROM THE TOOTH LOGO.

The store front is 6 windows roughly 60'' x 36'' The smaller windows below are 27'' x 36''. Around the corner there are 3 windows. they are 60'' x 27'' lower windows are 27" x 27". We would like to keep the bottom windows clear and keep the signage on the top windows, however, we are flexible.

The front 6 windows need to have this information worked into the design.

Practice name: Vesk and Ormond Dental & Orthodontics.
Phone numbers: Marisol Vesk DDS: 415.772.0183
Tobias Ormond DDS:415.509.2371

Expertise: Dr. Vesk General Dentistry & Orthodontics
Dr. Ormond Oral Surgery & Sedation

Address: 1937 Birchwood Ave

A banner across the bottom of the top windows with some key advertisement words: "Clarivet" "Braces" "Implants" "Whiting" "Call today" "Free Consultation" "Oral Surgery" "Sedation". We like the two color idea. Its up to you to decide on the color combo. I used a Dark and light blue, but maybe a Blue and grey would nice to tire in the logo colors?

I have made some mock ideas to get the ball rolling but you do not have to stick to these designs at all, just as long as all the required information is there. Be creative with the layouts, fonts, color scheme, (just remember these are going on windows not necessarily a white background), and graphics/artistic flare (refer to logo for layout inspiration and use the logo as an actual graphic). We are running a miltimillion dollar dental practice so we want these windows to be eye catching to pull in patients and look like a million dollar design. Also all 6 windows dont need ot be used. I am really looking for creative design marketing.

The corner 3 windows need the following information: name, expertise, phone number, banner.

Dr. Vesk, General Dentistry & Orthodontics, 415.772.0183
Dr. Ormond, Oral Surgery & Sedation, 415.509.2371

There is also a front door that needs to be designed. The door is 60'' x 36'' (standard door size) We want simple white vinyl on the outside of the door. We need you to organize the information on the door, pick a easy to read font, maybe use the logo and use some of the front window signage aesthetic? Its up to you...but we we were initially thinking of just making the litters white and keep it simple but again you are the designers.

Practice name: Vesk and Ormond General Dentistry & Orthodontics

Address: 1937 Birchwood Ave

Phone numbers: Dr. Vesk 415.772.0183
Dr. Ormond 415.509.2371

Hours of operation: Mon: call for an appointment
Tues-Thurs: 9am-5pm
Sat: call for an appointment
Sun: Closed

A line saying we speak Spanish: Se Habla Espanol

*****************************************************************************************************
here are some design that we liked and some rough sketches I made to start the ball rolling. Keep in mind that there are 9 windows for the front because its a corner office, but not all of them have to have stuff on it. We want simple, streamline, classy high commanding price point aesthetic. I am hiring you for your artistic minds.

Target Market(s)

anyone who has dental needs

Industry/Entity Type

Dental

Font styles to use
Serif
Sans Serif

Colors

Designer to choose colors to be used in the design.

Requirements
Must have
• 1. The required information (see project description)
• 2. Logo
• 3. Advertisement banner running along the bottom of all 9 windows (6 in front and 3 on the side)
• NOTE: Look at pictures of the store to get a sense of the customers point of view and also as a reference to how your design will be broken up across several windows or maybe you design something special for every window. But we want the banner to run along all the windows to lead customs to the door on the side. Finally the letters will be done in white vinyl unless state otherwise, remember the window needs to let in natural light so the entire window can not be covered in vinyl.
Nice to have
• artistic flare yet simple and sleep and expensive looking aesthetic. work logo into the design.
Should not have
• The goal is to catch someone eye and give them important information about the practice.
• It should not just be words.
• It should not have to many words
• It must be readable font for cards driving by.

```html
<!DOCTYPE html>
<html lang="en">
<head>
<meta charset="utf-8">
<title>Vesk and Ormond Dental &amp; Orthodontics — Storefront Windows</title>
<link href="https://fonts.googleapis.com/css2?family=Questrial&display=swap" rel="stylesheet">
<style>
  :root {
    --brand-blue: #1a62a3;
    --banner-blue: #0b5fa5;
    --pane-grey: #cdcdcd;
    --frame-grey: #c8c8c8;
    --ink: #0d0d0d;
    --glass: #ffffff;
  }
  html, body {
    margin: 0;
    padding: 0;
    width: 1200px;
    height: 759px;
    overflow: hidden;
    background: var(--glass);
    font-family: "Questrial", "Helvetica Neue", Arial, sans-serif;
  }
  .storefront {
    position: relative;
    width: 1200px;
    height: 759px;
  }
  .window-pane {
    position: absolute;
    top: 148px;
    width: 171px;
    height: 284px;
    border: 1px solid var(--frame-grey);
    box-sizing: border-box;
  }
  .banner-pane {
    position: absolute;
    top: 437px;
    width: 171px;
    height: 128px;
    background: var(--pane-grey);
    border-top: 5px solid var(--banner-blue);
    border-left: 1px solid var(--frame-grey);
    border-right: 1px solid var(--frame-grey);
    box-sizing: border-box;
    display: flex;
    align-items: center;
    justify-content: center;
    padding-bottom: 22px;
  }
  .banner-pane::after {
    content: "";
    position: absolute;
    left: 0; right: 0; bottom: 0;
    height: 21px;
    background: var(--banner-blue);
  }
  .banner-word {
    color: var(--brand-blue);
    font-size: 23px;
    letter-spacing: 0.5px;
    text-transform: uppercase;
    white-space: nowrap;
  }
  .col-1 { left: 75px; }
  .col-2 { left: 251px; }
  .col-3 { left: 427px; }
  .col-4 { left: 603px; }
  .col-5 { left: 779px; }
  .col-6 { left: 954px; }

  .mark-placeholder {
    position: absolute;
    left: 78px;
    top: 160px;
    width: 400px;
    height: 400px;
  }

  .practice-name {
    position: absolute;
    left: 518px;
    top: 202px;
    color: var(--brand-blue);
    margin: 0;
    font-weight: 400;
  }
  .practice-name .partners {
    display: block;
    font-size: 25px;
    letter-spacing: 14px;
    line-height: 1;
    text-transform: uppercase;
    white-space: nowrap;
  }
  .practice-name .specialty {
    display: block;
    margin-top: 12px;
    font-size: 36px;
    line-height: 1;
    white-space: nowrap;
  }
  .practice-name .specialty .amp { font-size: 26px; }

  .info-tag {
    position: absolute;
    top: 337px;
    height: 65px;
    background: var(--pane-grey);
    color: var(--brand-blue);
    text-align: center;
    display: flex;
    flex-direction: column;
    justify-content: center;
    line-height: 1.15;
  }
  .info-tag .line { font-size: 16.5px; white-space: nowrap; }
  .info-tag .small { font-size: 8px; line-height: 1.3; }
  .tag-dentistry { left: 470px; width: 128px; }
  .tag-vesk { left: 604px; width: 130px; }
  .tag-surgery { left: 821px; width: 128px; }
  .tag-ormond { left: 954px; width: 132px; }
</style>
</head>
<body>
<main class="storefront">

  <svg class="mark-placeholder" viewBox="0 0 400 400" role="img" aria-label="Space for the practice's tooth logo graphic">
    <circle cx="200" cy="200" r="190" fill="#d6d6d6"/>
  </svg>

  <div class="window-pane col-1"></div>
  <div class="window-pane col-2"></div>
  <div class="window-pane col-3"></div>
  <div class="window-pane col-4"></div>
  <div class="window-pane col-5"></div>
  <div class="window-pane col-6"></div>

  <h1 class="practice-name">
    <span class="partners">Vesk &nbsp;and&nbsp; Ormond</span>
    <span class="specialty">DENTAL <span class="amp">&amp;</span> ORTHODONTICS</span>
  </h1>

  <div class="info-tag tag-dentistry">
    <span class="line">Dentistry</span>
    <span class="small">&amp;</span>
    <span class="line">Orthodontics</span>
  </div>
  <div class="info-tag tag-vesk">
    <span class="line">Marisol Vesk</span>
    <span class="small">DDS</span>
    <span class="line">415.772.0183</span>
  </div>
  <div class="info-tag tag-surgery">
    <span class="line">Oral Surgery</span>
    <span class="small">&amp;</span>
    <span class="line">Sedation</span>
  </div>
  <div class="info-tag tag-ormond">
    <span class="line">Tobias Ormond</span>
    <span class="small">DDS</span>
    <span class="line">415.509.2371</span>
  </div>

  <div class="banner-pane col-1"></div>
  <div class="banner-pane col-2"></div>
  <div class="banner-pane col-3"><span class="banner-word">Clarivet</span></div>
  <div class="banner-pane col-4"><span class="banner-word">Braces</span></div>
  <div class="banner-pane col-5"><span class="banner-word">Implants</span></div>
  <div class="banner-pane col-6"><span class="banner-word">Whitening</span></div>

</main>
</body>
</html>
```